Boutique Wealth management firm needs a new business card design

I want to update my business card design to be more consistent with the look and feel of my website (www.brisvane-wealth.com). I would like to incorporate an ivory parchment background and am open to switching from the current "portrait" layout to a more traditional "landscape" orientation. The final design should convey stability and exclusivity and I want something in PDF format that is ready to send to the printer

Thank you all for taking the time to submit your designs for my project. I've made my decision and picked the design I like best. Thanks again!

```html
<!DOCTYPE html>
<html lang="en">
<head>
<meta charset="utf-8">
<title>Brisvane Wealth Advisory – Business Card</title>
<link rel="stylesheet" href="https://fonts.googleapis.com/css2?family=Arimo:wght@400;700&family=Open+Sans:wght@400;600;700&display=swap">
<style>
  :root {
    --stage: #ffffff;
    --ivory-light: #fbf4d8;
    --ivory: #f3e6b6;
    --ivory-deep: #e9d79c;
    --maroon: #6e2140;
    --maroon-soft: #7a2a48;
    --ink: #161616;
    --ink-deep: #0d0d0d;
    --cream-text: #f5eed6;
    --divider: #b9ab84;
  }
  * { box-sizing: border-box; margin: 0; padding: 0; }
  html, body {
    width: 1200px; height: 900px; overflow: hidden;
    background: var(--stage);
  }
  .card {
    position: absolute; left: 150px; top: 193px;
    width: 900px; height: 514px;
    border-radius: 30px; overflow: hidden;
    box-shadow: 0 10px 30px rgba(0,0,0,0.18);
    font-family: "Open Sans", sans-serif;
  }
  .card__parchment {
    position: absolute; left: 0; top: 0; width: 100%; height: 242px;
    background:
      radial-gradient(ellipse at 20% 30%, var(--ivory-light) 0%, transparent 55%),
      radial-gradient(ellipse at 75% 70%, var(--ivory-light) 0%, transparent 50%),
      radial-gradient(ellipse at 50% 0%, var(--ivory-deep) 0%, transparent 60%),
      var(--ivory);
  }
  .brand {
    position: absolute; right: 150px; top: 70px;
    text-align: right; color: var(--maroon); font-weight: 700;
    font-family: "Open Sans", sans-serif; line-height: 1;
  }
  .brand__name { font-size: 66px; letter-spacing: 1px; }
  .brand__sub { font-size: 33px; margin-top: 4px; }
  .tagline {
    position: absolute; left: 0; top: 242px; width: 100%; height: 26px;
    background: var(--maroon);
    color: var(--cream-text);
    font-size: 17px; letter-spacing: 17.5px; line-height: 26px;
    padding-left: 60px; white-space: nowrap;
  }
  .card__base {
    position: absolute; left: 0; top: 268px; width: 100%; height: 246px;
    background: linear-gradient(180deg, var(--ink) 0%, var(--ink-deep) 100%);
  }
  .person {
    position: absolute; right: 458px; top: 100px; text-align: right;
    font-family: "Arimo", sans-serif; font-weight: 700;
  }
  .person__name { color: var(--maroon-soft); font-size: 32px; }
  .person__name sup { font-size: 15px; }
  .person__role { color: var(--cream-text); font-size: 20px; margin-top: 2px; }
  .divider {
    position: absolute; left: 476px; top: 20px; width: 2px; height: 205px;
    background: var(--divider);
  }
  .contact {
    position: absolute; left: 504px; top: 18px;
    color: var(--cream-text); font-size: 20px; line-height: 28px; list-style: none;
  }
  .contact li { display: flex; align-items: flex-start; gap: 8px; }
  .contact svg { width: 22px; height: 22px; margin-top: 3px; flex: none; fill: var(--maroon-soft); }
  .contact .contact__address { margin-top: 12px; }
  .contact .contact__license { margin-top: 14px; padding-left: 30px; }
</style>
</head>
<body>
  <article class="card">
    <div class="card__parchment">
      <div class="brand">
        <div class="brand__name">BRISVANE</div>
        <div class="brand__sub">Wealth Advisory</div>
      </div>
    </div>
    <div class="tagline">GUIDING YOUR LIFE AND LEGACY</div>
    <div class="card__base">
      <div class="person">
        <div class="person__name">Dale Harlow, CFP<sup>®</sup></div>
        <div class="person__role">Principal</div>
      </div>
      <div class="divider"></div>
      <ul class="contact">
        <li>
          <svg viewBox="0 0 24 24" aria-hidden="true"><path d="M6.6 10.8a15 15 0 0 0 6.6 6.6l2.2-2.2a1 1 0 0 1 1-.25 11.4 11.4 0 0 0 3.6.57 1 1 0 0 1 1 1V20a1 1 0 0 1-1 1A17 17 0 0 1 3 4a1 1 0 0 1 1-1h3.5a1 1 0 0 1 1 1c0 1.25.2 2.46.57 3.6a1 1 0 0 1-.25 1z"/></svg>
          <span>925-555-0182</span>
        </li>
        <li>
          <svg viewBox="0 0 24 24" aria-hidden="true"><path d="M3 6h18v12H3z M3 6l9 7 9-7" fill="none" stroke="#7a2a48" stroke-width="2"/></svg>
          <span>dale@brisvane-wealth.com</span>
        </li>
        <li>
          <svg viewBox="0 0 24 24" aria-hidden="true"><g fill="none" stroke="#7a2a48" stroke-width="1.8"><circle cx="12" cy="12" r="9"/><ellipse cx="12" cy="12" rx="4" ry="9"/><path d="M3 12h18M5 7h14M5 17h14"/></g></svg>
          <span>www.brisvane-wealth.com</span>
        </li>
        <li class="contact__address">
          <svg viewBox="0 0 24 24" aria-hidden="true"><path d="M12 3 2 12h3v8h5v-5h4v5h5v-8h3z"/></svg>
          <span>218 Alder Ridge Rd. #412<br>Fairbrook, CA 94560</span>
        </li>
        <li class="contact__license">CA Insurance License #0K71836</li>
      </ul>
    </div>
  </article>
</body>
</html>
```